Vodka Carton Design

We need a design completed for our 6x700ml vodka carton.
We currently have a bottle label designed and would like an outer packaging design created for the 6 x 700ml vodka carton.

We would like the packaging design to be similar to our current bottle label design for consistency in our product branding but artistic freedom and variation is encouraged. (images of bottle have been attached)

Certain particulars and compulsory elements for the design have been outlined below.

The dimensions of the carton are
H = 320mm
L=224mm
W = 150mm

- Due to industry requirements, the label must have the following design elements included

- a pregnancy warning label with the correct sizing on the design (requirements attached and high def image of decal attached)

- barcode (attached)

The name of the vodka product is called
"Kestrel Vodka - Heritage Range" and our company name is called
"Kestrel Distilling Co" (logos attached)

Good luck !

Need extra days to review

```html
<!DOCTYPE html>
<html lang="en">
<head>
<meta charset="utf-8">
<title>Kestrel Vodka – Heritage Range 6x700ml Carton Dieline</title>
<link href="https://fonts.googleapis.com/css2?family=Zilla+Slab:wght@600;700&family=Poppins:wght@400;500;600&family=Petit+Formal+Script&display=swap" rel="stylesheet">
<style>
  :root{
    --paper:#ffffff;
    --backdrop:#ffffff;
    --ink:#2d2624;
    --royal:#2e3192;
    --warning-red:#e3191f;
    --cut-line:#9a9a9a;
    --code-area:#e4e4e4;
  }
  html,body{margin:0;padding:0;width:1104px;height:1200px;overflow:hidden;background:var(--backdrop);}
  .canvas{position:relative;width:1104px;height:1200px;}
  .dieline{position:absolute;left:0;top:12px;width:1104px;height:669px;}
  .panel{fill:var(--paper);stroke:var(--cut-line);stroke-width:1;}
  .fold{stroke:var(--cut-line);stroke-width:1;}
  .band{fill:var(--ink);}
  .ribbon{fill:var(--royal);}
  .ribbon-trim{fill:none;stroke:#fff;stroke-width:2.5;}
  .serif{font-family:'Zilla Slab',Georgia,serif;font-weight:700;fill:var(--ink);text-anchor:middle;}
  .sans{font-family:'Poppins',Arial,sans-serif;fill:var(--ink);text-anchor:middle;}
  .script{font-family:'Petit Formal Script',cursive;fill:var(--ink);text-anchor:middle;}
  .brand-small{font-size:25px;letter-spacing:6px;}
  .brand-large{font-size:52px;letter-spacing:9px;}
  .range-label{font-family:'Poppins',Arial,sans-serif;font-weight:500;fill:#fff;text-anchor:middle;}
  .body-copy{font-size:14.5px;font-weight:500;}
  .company{font-size:17px;font-weight:600;letter-spacing:1.6px;}
  .web{font-size:14.5px;font-weight:600;}
  .address{font-size:11.5px;font-weight:500;}
  .warning-title{font-family:'Poppins',Arial,sans-serif;font-weight:600;font-size:12.5px;fill:var(--warning-red);}
  .warning-text{font-family:'Poppins',Arial,sans-serif;font-size:12px;fill:var(--ink);}
  .icon-box{fill:#fff;stroke:var(--ink);stroke-width:2.5;}
  .icon{fill:none;stroke:var(--ink);stroke-width:3;stroke-linecap:round;stroke-linejoin:round;}
  .barcode-area{fill:var(--code-area);stroke:var(--ink);stroke-width:1;}
  .ribbon-name{font-family:'Poppins',Arial,sans-serif;font-size:12px;fill:#fff;text-anchor:middle;}
  .spec{font-family:'Poppins',Arial,sans-serif;font-size:21px;fill:var(--ink);text-anchor:middle;}
  .count{font-family:'Poppins',Arial,sans-serif;font-weight:500;fill:#fff;text-anchor:middle;}
</style>
</head>
<body>
<main class="canvas">
<svg class="dieline" viewBox="100 85 1650 1000" xmlns="http://www.w3.org/2000/svg">
  <g class="net">
    <rect class="panel" x="110" y="250" width="63" height="668"/>
    <rect class="panel" x="173" y="93" width="1565" height="983"/>
    <line class="fold" x1="173" y1="250" x2="1738" y2="250"/>
    <line class="fold" x1="173" y1="918" x2="1738" y2="918"/>
    <line class="fold" x1="487" y1="93" x2="487" y2="1076"/>
    <line class="fold" x1="956" y1="93" x2="956" y2="1076"/>
    <line class="fold" x1="1270" y1="93" x2="1270" y2="1076"/>
    <rect class="band" x="173" y="250" width="1565" height="24"/>
    <rect class="band" x="173" y="895" width="1565" height="23"/>
  </g>

  <defs>
    <g id="side-panel">
      <text class="serif brand-small" x="330" y="310">KESTREL</text>
      <text class="serif brand-large" x="332" y="360">VODKA</text>
      <rect class="band" x="212" y="376" width="236" height="42"/>
      <text class="range-label" x="330" y="404" font-size="18" letter-spacing="3">HERITAGE RANGE</text>

      <text class="sans body-copy" x="330" y="458">This smooth, clean tasting Vodka</text>
      <text class="sans body-copy" x="330" y="479">is perfect on its own, over ice,</text>
      <text class="sans body-copy" x="330" y="500">or any cocktail.</text>
      <text class="script" x="326" y="538" font-size="17">Distilled and bottled by</text>
      <text class="sans company" x="330" y="562">KESTREL DISTILLING CO.</text>
      <text class="sans web" x="330" y="604">www.kestreldistillingco.com.au</text>
      <text class="sans address" x="330" y="620">14/8 wren lane, Ashfield Park 6021 wa</text>

      <g class="pregnancy-warning">
        <rect x="226" y="646" width="208" height="47" fill="#fff" stroke="var(--ink)" stroke-width="1.5"/>
        <circle cx="248" cy="669" r="15" fill="#fff" stroke="var(--warning-red)" stroke-width="4"/>
        <line x1="238" y1="659" x2="258" y2="679" stroke="var(--warning-red)" stroke-width="4"/>
        <text class="warning-title" x="270" y="662">PREGNANCY WARNING</text>
        <text class="warning-text" x="270" y="675">Alcohol can cause lifelong</text>
        <text class="warning-text" x="270" y="687">harm to your baby</text>
      </g>

      <g class="handling-icons">
        <rect class="icon-box" x="230" y="714" width="44" height="44" rx="6"/>
        <path class="icon" d="M243 748V725M237 731l6-7 6 7M259 748V725M253 731l6-7 6 7M237 750h28"/>
        <rect class="icon-box" x="282" y="714" width="44" height="44" rx="6"/>
        <path d="M286 738a18 16 0 0 1 36 0z" fill="var(--ink)"/>
        <path class="icon" d="M304 738v12a3 3 0 0 1-6 0"/>
        <rect class="icon-box" x="334" y="714" width="44" height="44" rx="6"/>
        <path d="M346 722h20l-2 14a8 8 0 0 1-16 0z" fill="var(--ink)"/>
        <path class="icon" d="M356 744v9M349 753h14"/>
        <rect class="icon-box" x="386" y="714" width="44" height="44" rx="6"/>
        <path class="icon" d="M402 726l6-4 6 8M418 736l4 8-8 5M400 748l-8-2 3-9"/>
      </g>

      <g class="standard-drinks">
        <text class="sans" x="221" y="789" font-size="20" font-weight="500">6x</text>
        <path d="M191 794h61l-9 63h-43z" fill="#fff" stroke="var(--ink)" stroke-width="2"/>
        <text class="sans" x="221" y="803" font-size="8.5">STANDARD</text>
        <text class="sans" x="221" y="812" font-size="8.5">DRINKS</text>
        <text class="sans" x="221" y="843" font-size="30" font-weight="500">21</text>
        <text class="sans" x="221" y="854" font-size="7">APPROX.</text>
      </g>

      <rect class="barcode-area" x="264" y="777" width="130" height="98" role="img" aria-label="Reserved area for the product barcode"/>

      <g class="carton-weight">
        <rect x="433" y="795" width="17" height="16" rx="2" fill="none" stroke="var(--ink)" stroke-width="4"/>
        <path d="M421 810h41l13 47h-67z" fill="var(--ink)"/>
        <text class="count" x="442" y="842" font-size="17">7,5kg</text>
      </g>
    </g>

    <g id="front-panel">
      <g class="top-ribbon">
        <path class="ribbon" d="M658 93h126v335l-63-38-63 38z"/>
        <path class="ribbon-trim" d="M664 93v322l57-34 57 34V93"/>
        <circle cx="721" cy="152" r="28" fill="none" stroke="#fff" stroke-width="2"/>
        <text class="ribbon-name" x="721" y="205">KESTREL</text>
        <text class="ribbon-name" x="721" y="218">DISTILLING CO.</text>
        <circle cx="721" cy="298" r="28" fill="none" stroke="#fff" stroke-width="2"/>
        <text class="ribbon-name" x="721" y="352">KESTREL</text>
        <text class="ribbon-name" x="721" y="365">DISTILLING CO.</text>
      </g>

      <text class="serif" x="721" y="522" font-size="40" letter-spacing="3">KESTREL</text>
      <text class="serif" x="723" y="601" font-size="33" letter-spacing="7">KESTREL</text>
      <text class="serif" x="723" y="668" font-size="72" letter-spacing="13">VODKA</text>

      <g class="bottom-ribbon">
        <path class="ribbon" d="M658 700l63 45 63-45v218H658z"/>
        <path class="ribbon-trim" d="M661 918V707l60 40 60-40v211"/>
      </g>
      <rect class="band" x="533" y="785" width="377" height="42"/>
      <text class="range-label" x="722" y="815" font-size="22" letter-spacing="4">HERITAGE RANGE</text>
      <text class="spec" x="585" y="853">35,5 %</text>
      <text class="spec" x="585" y="878">ALC/VOL</text>
      <text class="spec" x="858" y="853">BATCH#</text>
      <text class="count" x="721" y="876" font-size="52">6x</text>
      <text class="count" x="721" y="896" font-size="17" font-weight="400">700 ml</text>
    </g>
  </defs>

  <use href="#side-panel"/>
  <use href="#front-panel"/>
  <use href="#side-panel" transform="translate(782 0)"/>
  <use href="#front-panel" transform="translate(782 0)"/>
</svg>
</main>
</body>
</html>
```